Price Calculator as Responsive Web App to support Sales People

We need to build a simple micro web app to support sales people in making quotes. We already have a backend that can take a number of parameters and create a quote. We need put a responsive web app on top of this so that our people on the road can easily do their price simulations.

We need two pages. One for the input and another for the results. No menus, navigations, etc. It is 6 different inputs as shown with boxes in the sketch. They don't need to be boxed, but some of them have a bit of instruction text that clearly need to belong to the input.

This needs to be responsive, but first and foremost designed for smartphones. I have included a background gradient that we would like to use -- or a variant of it. We expect this to be delivered as HTML/CSS + images so that we can quickly write a few pieces of JavaScript ourselves to wire it up to our price simulator.

Industry/Entity Type

Information Technology

Coding

Coded - Design and coding required

Number of Pages Required

2 page

Font styles to use
Sans Serif

Requirements
Must have
• Responsive design
• Easy to wire up JavaScript to the HTML/CSS
Nice to have
• Some quick way to pick number of months. +/- buttons to add remove a year or 3 months. Same thing with number of items. Add 10 or 5 quickly.
• Maybe some parallax effect while scrolling as long as it is not distracting.
Should not have
• Toolbars, Menus, Navigations, Banners, etc. This is just a single micro app.

```html
<!DOCTYPE html>
<html lang="en">
<head>
<meta charset="utf-8">
<title>Price Calculator – Input</title>
<link rel="stylesheet" href="https://fonts.googleapis.com/css2?family=Montserrat:wght@400;500;600;700&family=Open+Sans:wght@400;500&display=swap">
<style>
  :root {
    --bg-deep: #01213d;
    --bg-mid: #06527c;
    --ink: #0f2236;
    --brand: #0a4870;
    --brand-dark: #032c4c;
    --brand-light: #0f5d8c;
    --rule: #dcdfe3;
    --paper: #ffffff;
  }
  * { box-sizing: border-box; margin: 0; padding: 0; }
  html, body { width: 1200px; height: 1120px; overflow: hidden; }
  body {
    font-family: "Montserrat", sans-serif;
    color: var(--ink);
    background: linear-gradient(180deg, var(--bg-deep) 0%, #023a61 30%, var(--bg-mid) 52%, #023a61 75%, var(--bg-deep) 100%);
    position: relative;
  }
  .calculator {
    position: absolute;
    left: 260px; top: 77px;
    width: 678px; height: 952px;
    background: var(--paper);
    padding: 17px 40px 0 30px;
  }
  .field {
    padding: 12px 0 12px;
    border-bottom: 1px solid var(--rule);
  }
  .field:first-child, .field:nth-child(2) { padding-bottom: 16px; }
  .field-label {
    font-size: 14px; font-weight: 500;
    line-height: 20px;
    letter-spacing: 0.1px;
  }
  .stepper {
    display: flex;
    margin: 11px 0 0 2px;
    width: 286px; height: 32px;
    border-radius: 16px;
    overflow: hidden;
    background: linear-gradient(180deg, var(--brand-light), var(--brand-dark));
  }
  .stepper-btn {
    width: 46px;
    border: 0;
    background: transparent;
    color: #fff;
    font: 700 13px "Montserrat", sans-serif;
    letter-spacing: 0.5px;
  }
  .stepper-btn + .stepper-btn { border-left: 1px solid rgba(0,0,0,0.35); }
  .stepper-value {
    width: 102px;
    margin: 2px 0;
    background: var(--paper);
    display: flex; align-items: center; justify-content: center;
    font-size: 13px; font-weight: 700; letter-spacing: 0.4px;
  }
  .options { margin-top: 4px; list-style: none; }
  .option {
    height: 32px;
    display: flex; align-items: center;
    font-size: 13px; letter-spacing: 0.2px;
    position: relative;
    white-space: nowrap;
  }
  .option input { position: absolute; opacity: 0; }
  .radio-mark {
    flex: none;
    width: 21px; height: 21px;
    margin-left: 2px; margin-right: 9px;
    border: 2px solid var(--brand-dark);
    border-radius: 50%;
    display: flex; align-items: center; justify-content: center;
  }
  .option input:checked + .radio-mark::after {
    content: ""; width: 11px; height: 11px; border-radius: 50%;
    background: var(--brand-dark);
  }
  .hint {
    position: relative;
    margin-left: 13px;
    height: 32px; padding: 0 18px 0 20px;
    border-radius: 16px;
    background: var(--brand);
    color: #fff;
    font: 400 10px "Open Sans", sans-serif;
    letter-spacing: 0;
    display: flex; align-items: center;
  }
  .hint::before {
    content: ""; position: absolute; left: -5px; top: 12px;
    border-style: solid; border-width: 4px 6px 4px 0;
    border-color: transparent var(--brand) transparent transparent;
  }
  .next-btn {
    margin: 24px 0 0 2px;
    width: 137px; height: 38px;
    border: 0; border-radius: 19px;
    background: linear-gradient(180deg, var(--brand-light), var(--brand-dark));
    color: #fff;
    display: flex; align-items: center;
    font: 700 10px "Montserrat", sans-serif;
    letter-spacing: 2.6px;
  }
  .next-label { width: 95px; text-align: center; padding-left: 4px; }
  .next-divider { width: 1px; height: 22px; background: rgba(255,255,255,0.35); }
  .next-icon { margin-left: 12px; }
</style>
</head>
<body>
<form class="calculator">
  <section class="field">
    <h2 class="field-label">Duration</h2>
    <div class="stepper">
      <button type="button" class="stepper-btn">-1</button>
      <button type="button" class="stepper-btn">-12</button>
      <output class="stepper-value">24 months</output>
      <button type="button" class="stepper-btn">+12</button>
      <button type="button" class="stepper-btn">+1</button>
    </div>
  </section>

  <section class="field">
    <h2 class="field-label">Count</h2>
    <div class="stepper">
      <button type="button" class="stepper-btn">-1</button>
      <button type="button" class="stepper-btn">-10</button>
      <output class="stepper-value">100 items</output>
      <button type="button" class="stepper-btn">+10</button>
      <button type="button" class="stepper-btn">+1</button>
    </div>
  </section>

  <section class="field">
    <h2 class="field-label">Engine Power (beyond standard)</h2>
    <ul class="options">
      <li><label class="option"><input type="radio" name="engine" checked><span class="radio-mark"></span><span class="option-text">$360 / year - bronze power</span><span class="hint">the basic engine, lorem ipsum...</span></label></li>
      <li><label class="option"><input type="radio" name="engine"><span class="radio-mark"></span>$600 / year - silver power</label></li>
      <li><label class="option"><input type="radio" name="engine"><span class="radio-mark"></span>$1M / year - gold power</label></li>
      <li><label class="option"><input type="radio" name="engine"><span class="radio-mark"></span>$3M / year - platinum power</label></li>
    </ul>
  </section>

  <section class="field">
    <h2 class="field-label">Shared storage addition</h2>
    <ul class="options">
      <li><label class="option"><input type="radio" name="storage" checked><span class="radio-mark"></span>10kg</label></li>
      <li><label class="option"><input type="radio" name="storage"><span class="radio-mark"></span>50kg</label></li>
      <li><label class="option"><input type="radio" name="storage"><span class="radio-mark"></span>100kg</label></li>
      <li><label class="option"><input type="radio" name="storage"><span class="radio-mark"></span>500kg</label></li>
      <li><label class="option"><input type="radio" name="storage"><span class="radio-mark"></span>1 ton</label></li>
    </ul>
  </section>

  <section class="field">
    <h2 class="field-label">Additional Tip</h2>
    <ul class="options">
      <li><label class="option"><input type="radio" name="tip" checked><span class="radio-mark"></span>15%</label></li>
      <li><label class="option"><input type="radio" name="tip"><span class="radio-mark"></span>18%</label></li>
      <li><label class="option"><input type="radio" name="tip"><span class="radio-mark"></span>20%</label></li>
    </ul>
  </section>

  <section class="field">
    <h2 class="field-label">Elastic extension</h2>
    <ul class="options">
      <li><label class="option"><input type="radio" name="elastic" checked><span class="radio-mark"></span>30%</label></li>
      <li><label class="option"><input type="radio" name="elastic"><span class="radio-mark"></span>50%</label></li>
    </ul>
  </section>

  <button type="submit" class="next-btn">
    <span class="next-label">NEXT</span>
    <span class="next-divider"></span>
    <svg class="next-icon" width="8" height="14" viewBox="0 0 8 14" aria-hidden="true">
      <path d="M1 1l6 6-6 6" fill="none" stroke="#fff" stroke-width="1.6" stroke-linecap="round" stroke-linejoin="round"/>
    </svg>
  </button>
</form>
</body>
</html>
```